Multi-Specialty, Outpatient, Physical Therapy Clinic needs new Personal Injury Patient brochure

Coastal Motion & Posture Care.
We have 3 outpatient, physical therapy clinics that also offer Chiropractic Care and Medical Massage under one roof. We have 3 target patient types but want to focus this design specifically on Personal Injury (auto accident) patients. We want a tri-fold, color brochure for promotional purposes.

Target Market(s)

Personal Injury patients

Industry/Entity Type

Physical Therapy

Font styles to use
Serif

Requirements
Must have
• Tri-Fold brochure style, CMPC logo, information about our service (physical therapy, chiropractic care, medical massage), 3 office location addresses & phone numbers:
• 4817 Gullwing Rd
• Indian Harbour Beach, FL 32955
• (321) 555-0147
• 5726 E. Marlowe Blvd. #214
• Titusville, FL 32796
• (321) 555-0182
• 8140 W. Tamberly Rd. #327
• Melbourne, FL 32968
• (321) 555-0139
Nice to have
• graphics that would apply to the patients we're targeting

```html
<!DOCTYPE html>
<html lang="en">
<head>
<meta charset="utf-8">
<title>Coastal Motion &amp; Posture Care – Personal Injury Brochure</title>
<link rel="stylesheet" href="https://fonts.googleapis.com/css2?family=Oswald:wght@400;500;600&family=Open+Sans:wght@400;600;700&display=swap">
<style>
:root{
  --blue:#1f63b5;
  --navy:#163e78;
  --sky:#dbe8f6;
  --pale:#f1f5fa;
  --orange:#f29a1f;
  --green:#78b940;
  --ink:#3c4654;
  --white:#ffffff;
  --page:#eeeeee;
}
*{box-sizing:border-box;margin:0;padding:0}
html,body{width:874px;height:1200px;overflow:hidden;background:var(--page)}
body{position:relative;font-family:"Open Sans",Arial,sans-serif;color:var(--ink)}
.sheet{position:absolute;left:45px;width:784px;height:560px;display:flex;background:var(--white);box-shadow:0 2px 8px rgba(0,0,0,.18)}
.sheet--outside{top:25px}
.sheet--inside{top:612px;flex-wrap:wrap;align-content:flex-start}
.panel{position:relative;width:261.33px;height:100%;overflow:hidden}
.heading{font-family:"Oswald",Arial,sans-serif;font-weight:500;text-transform:uppercase;letter-spacing:.3px}
.band{background:var(--blue);color:var(--white);text-align:center}

/* outside – left panel */
.care-panel{background:var(--pale)}
.care-header{height:118px;background:var(--blue);color:var(--white);padding:22px 20px 0;text-align:center;font-size:15px;line-height:1.3;border-bottom-left-radius:50% 26px;border-bottom-right-radius:50% 26px}
.check-list{list-style:none;padding:22px 26px 0}
.check-list li{display:flex;gap:7px;align-items:flex-start;font-size:7px;line-height:1.35;font-weight:600;text-transform:uppercase;margin-bottom:11px;color:var(--ink)}
.check-list svg{flex:none;width:9px;height:9px;margin-top:1px}
.wave{position:absolute;left:0;bottom:0;width:100%;height:70px}

/* outside – middle panel */
.locations-panel{padding:60px 24px 0;text-align:center}
.pin{width:30px;height:30px;margin:0 auto 10px}
.locations-title{color:var(--blue);font-size:14px;line-height:1.3;margin-bottom:18px}
.location{margin-bottom:16px}
.pill{display:inline-block;background:var(--orange);color:var(--white);font-family:"Oswald",Arial,sans-serif;font-size:8px;letter-spacing:.5px;padding:3px 12px;border-radius:2px;margin-bottom:6px;text-transform:uppercase}
.location p{font-size:7.5px;line-height:1.5;font-weight:600}
.phone-band{position:absolute;left:0;right:0;bottom:0;height:62px;background:var(--blue);color:var(--white);display:flex;flex-direction:column;justify-content:center;align-items:center;font-size:8px}
.phone-band strong{font-family:"Oswald",Arial,sans-serif;font-size:15px;font-weight:500}

/* outside – cover */
.cover-panel{background:var(--white)}
.cover-photo{height:150px;background:linear-gradient(135deg,#c9d8ea,#8fb1d8 60%,#5d88bf)}
.cover-title{padding:14px 20px;font-size:15px;line-height:1.25}
.cover-images{display:flex;gap:6px;justify-content:center;padding:18px 18px 0}
.cover-images div{width:68px;height:60px;border-radius:3px;background:linear-gradient(160deg,#20406f,#3a6fb3 70%,#e6853a)}
.brand{display:flex;align-items:center;justify-content:center;gap:8px;margin-top:30px}
.brand-mark{width:20px;height:20px;border-radius:50%;background:var(--blue)}
.brand-name{font-family:"Oswald",Arial,sans-serif;font-weight:500;font-size:14px;color:var(--navy);line-height:1.15;max-width:130px}
.cover-phone{position:absolute;left:0;right:0;bottom:0;height:62px;display:flex;align-items:center;justify-content:center;gap:8px;font-family:"Oswald",Arial,sans-serif;font-size:18px;border-top-left-radius:50% 20px;border-top-right-radius:50% 20px}
.cover-phone svg{width:16px;height:16px}

/* inside */
.inside-header{width:100%;height:52px;background:var(--navy);color:var(--white);display:flex;align-items:center;justify-content:flex-end;padding-right:200px;font-size:22px}
.inside-sheet-body{display:flex;width:100%;height:508px}
.team-photo{height:150px;background:linear-gradient(180deg,#e7eef7,#b9cde6)}
.section-band{padding:9px 12px;font-size:14px;line-height:1.2}
.team-list{padding:12px 22px 0}
.team-group{margin-bottom:9px}
.team-group .pill{font-size:7px;margin-bottom:3px}
.team-group p{font-size:7px;line-height:1.45;font-weight:600}
.intro{padding:14px 20px 10px;font-size:7px;line-height:1.5;text-align:justify}
.services{padding:10px 20px 0}
.service{margin-bottom:8px}
.service .tag{display:block;color:var(--white);font-family:"Oswald",Arial,sans-serif;font-size:7.5px;letter-spacing:.4px;padding:2px 8px;margin-bottom:3px;text-transform:uppercase}
.tag--orange{background:var(--orange)}
.tag--green{background:var(--green)}
.service p{font-size:6.5px;line-height:1.45}
.therapy-panel{background:var(--pale)}
.therapy-panel .services{padding-top:16px}
</style>
</head>
<body>

<section class="sheet sheet--outside">
  <div class="panel care-panel">
    <h2 class="care-header heading">Providing exceptional care and customer service</h2>
    <ul class="check-list">
      <li><svg viewBox="0 0 10 10"><path d="M1 5l3 3 5-7" fill="none" stroke="#1f63b5" stroke-width="2"/></svg>Same day or next day appointments</li>
      <li><svg viewBox="0 0 10 10"><path d="M1 5l3 3 5-7" fill="none" stroke="#1f63b5" stroke-width="2"/></svg>Bilingual staff available</li>
      <li><svg viewBox="0 0 10 10"><path d="M1 5l3 3 5-7" fill="none" stroke="#1f63b5" stroke-width="2"/></svg>Clear and timely reports for every case</li>
      <li><svg viewBox="0 0 10 10"><path d="M1 5l3 3 5-7" fill="none" stroke="#1f63b5" stroke-width="2"/></svg>Regular updates on patient progress</li>
      <li><svg viewBox="0 0 10 10"><path d="M1 5l3 3 5-7" fill="none" stroke="#1f63b5" stroke-width="2"/></svg>Direct line to our records team</li>
      <li><svg viewBox="0 0 10 10"><path d="M1 5l3 3 5-7" fill="none" stroke="#1f63b5" stroke-width="2"/></svg>Pain management specialists</li>
      <li><svg viewBox="0 0 10 10"><path d="M1 5l3 3 5-7" fill="none" stroke="#1f63b5" stroke-width="2"/></svg>Free transport to appointments</li>
      <li><svg viewBox="0 0 10 10"><path d="M1 5l3 3 5-7" fill="none" stroke="#1f63b5" stroke-width="2"/></svg>Medical records delivered promptly</li>
      <li><svg viewBox="0 0 10 10"><path d="M1 5l3 3 5-7" fill="none" stroke="#1f63b5" stroke-width="2"/></svg>Evening and weekend hours at all offices</li>
      <li><svg viewBox="0 0 10 10"><path d="M1 5l3 3 5-7" fill="none" stroke="#1f63b5" stroke-width="2"/></svg>Three convenient locations</li>
    </ul>
    <svg class="wave" viewBox="0 0 261 70" preserveAspectRatio="none">
      <path d="M0 30 Q130 0 261 30 V70 H0Z" fill="#f29a1f"/>
      <path d="M0 42 Q130 14 261 42 V70 H0Z" fill="#1f63b5"/>
    </svg>
  </div>

  <div class="panel locations-panel">
    <svg class="pin" viewBox="0 0 30 30"><circle cx="15" cy="15" r="15" fill="#1f63b5"/><path d="M15 6a6 6 0 0 0-6 6c0 5 6 12 6 12s6-7 6-12a6 6 0 0 0-6-6z" fill="#fff"/><circle cx="15" cy="12" r="2.2" fill="#1f63b5"/></svg>
    <h2 class="locations-title heading">We are here when your<br>clients need us.</h2>
    <div class="location">
      <span class="pill">Indian Harbour Beach</span>
      <p>4817 Gullwing Rd<br>Indian Harbour Beach, FL 32955<br>(321) 555-0147</p>
    </div>
    <div class="location">
      <span class="pill">Titusville</span>
      <p>5726 E. Marlowe Blvd. #214<br>Titusville, FL 32796<br>(321) 555-0182</p>
    </div>
    <div class="location">
      <span class="pill">Melbourne</span>
      <p>8140 W. Tamberly Rd. #327<br>Melbourne, FL 32968<br>(321) 555-0139</p>
    </div>
    <div class="phone-band">
      <span>Call one number for every office</span>
      <strong>(321) 555-PAIN</strong>
    </div>
  </div>

  <div class="panel cover-panel">
    <div class="cover-photo" role="img" aria-label="Photo of a physician consulting with a patient"></div>
    <h1 class="cover-title band heading">Personal injury<br>medical care specialists</h1>
    <div class="cover-images">
      <div role="img" aria-label="Image of a neck injury highlighted in orange"></div>
      <div role="img" aria-label="Image of a spine with lower back pain"></div>
      <div role="img" aria-label="Image of a shoulder injury highlighted in orange"></div>
    </div>
    <div class="brand">
      <span class="brand-mark"></span>
      <span class="brand-name">Coastal Motion &amp; Posture Care</span>
    </div>
    <div class="cover-phone band">
      <svg viewBox="0 0 16 16"><path d="M3 1l3 3-2 2a9 9 0 0 0 6 6l2-2 3 3-2 2C7 15 1 9 1 3z" fill="#fff"/></svg>
      (321) 555-PAIN
    </div>
  </div>
</section>

<section class="sheet sheet--inside">
  <h2 class="inside-header heading">75,000 + treatments provided</h2>
  <div class="inside-sheet-body">
    <div class="panel">
      <div class="team-photo" role="img" aria-label="Photo of the clinic's medical team in white coats"></div>
      <h3 class="section-band band heading">Medical team</h3>
      <div class="team-list">
        <div class="team-group"><span class="pill">Medical doctors</span><p>Dr. Alan Reeve, MD<br>Dr. Nora Castell, DO</p></div>
        <div class="team-group"><span class="pill">Physical therapists</span><p>Janet Holm, DPT<br>Marco Ruiz, PT<br>Lena Ortiz, DPT</p></div>
        <div class="team-group"><span class="pill">Chiropractors</span><p>Dr. Owen Pratt, DC<br>Dr. Tessa Vail, DC</p></div>
        <div class="team-group"><span class="pill">Massage therapists</span><p>Cara Lind, LMT<br>Ben Soto, LMT</p></div>
      </div>
    </div>

    <div class="panel">
      <p class="intro">Our physicians have over 75 years of combined experience in the field of personal injury care. We work with patients and attorneys to deliver timely treatment, clear documentation and steady progress reports. Every plan is built around the patient's recovery, comfort and return to daily life after an accident.</p>
      <h3 class="section-band band heading">Physician supervised<br>services available</h3>
      <div class="services">
        <div class="service"><span class="tag tag--orange">Pain management</span><p>Injections and medication care for lasting relief of pain.</p></div>
        <div class="service"><span class="tag tag--orange">Diagnostic imaging / X-ray</span><p>On-site imaging for quick and accurate diagnosis.</p></div>
        <div class="service"><span class="tag tag--orange">Orthopedic care</span><p>Joint and bone evaluation by board certified doctors.</p></div>
        <div class="service"><span class="tag tag--orange">Neurology</span><p>Testing for nerve damage, numbness and headaches.</p></div>
        <div class="service"><span class="tag tag--orange">Case management</span><p>One contact to coordinate care, records and billing.</p></div>
      </div>
    </div>

    <div class="panel therapy-panel">
      <div class="services">
        <div class="service"><span class="tag tag--green">Physical therapy</span><p>Guided exercise and hands-on care to restore strength, balance and motion.</p></div>
        <div class="service"><span class="tag tag--green">Chiropractic care</span><p>Gentle spinal adjustments that ease pain and improve alignment.</p></div>
        <div class="service"><span class="tag tag--green">Medical massage</span><p>Targeted soft tissue work that relaxes muscles and speeds healing.</p></div>
        <div class="service"><span class="tag tag--green">Medical rehab</span><p>Structured programs that help patients return to work and home life.</p></div>
        <div class="service"><span class="tag tag--green">Spinal decompression</span><p>Non-surgical relief for disc injuries and lasting back pain.</p></div>
        <div class="service"><span class="tag tag--green">Post trauma training</span><p>Personal reconditioning to rebuild confidence after an accident.</p></div>
      </div>
    </div>
  </div>
</section>

</body>
</html>
```